Landscape Supplier and Excavation company needing a website revamp.

We need a web design for our company based out of northern Virginia. We make and deliver topsoil, mulch, and compost. We are also an excavation company. We provide a wide variety of excavation services, from residential to large commercial projects. We specialize in land clearing and building site preparation. We would like a site that looks very professional and makes us look like a large company. We've been in business since 1994 and have never had a really nice website. Our current website it www.hollowbrookloam.com and www.rkqmo.com for references. I like the information on the pages but would like something more professional looking. Doesn't HAVE to be 4 different pages, but I would like a contact form, our services, and our products/ pricing listed. We are properly licensed and insured and would like this included somewhere on the site.

Target Market(s)

Landscapers, Home Owners, Commercial

Industry/Entity Type

Excavation and Landscape Products Supplier

Number of Pages Required

4 page

Colors

Designer to choose colors to be used in the design.

Requirements
Must have
• Professional Look and Feel

```html
<!DOCTYPE html>
<html lang="en">
<head>
<meta charset="utf-8">
<title>Hollowbrook Loam and Excavation — About</title>
<link href="https://fonts.googleapis.com/css2?family=Montserrat:wght@600;700;800&family=Josefin+Sans:wght@300;400;600&display=swap" rel="stylesheet">
<style>
:root{
  --red:#b5202b;
  --ink:#141414;
  --ink-2:#1c1c1c;
  --ink-3:#0f0f0f;
  --paper:#ffffff;
  --board:#efefef;
  --light:#bdbdbd;
  --tone-mulch-a:#6e3024;
  --tone-mulch-b:#4e2219;
  --tone-land-a:#7b8063;
  --tone-land-b:#6f5a4c;
  --tone-steel-a:#c8c4bf;
  --tone-steel-b:#a27a60;
  --tone-sky-a:#8ea8bf;
  --tone-sky-b:#a8977c;
}
*{box-sizing:border-box;margin:0;padding:0}
html,body{width:1200px;height:2457px;overflow:hidden}
body{background:var(--board);font-family:"Josefin Sans",sans-serif;color:var(--ink);position:relative}
.label{position:absolute;top:70px;font:400 13px "Montserrat",sans-serif;letter-spacing:8px;color:#222}
.label-desktop{left:50px;width:820px;text-align:center}
.label-mobile{left:920px;width:230px;text-align:center}

.screen{position:absolute;top:120px;background:var(--paper);box-shadow:0 4px 18px rgba(0,0,0,.12);overflow:hidden}
.photo{display:block}
.mulch{background:linear-gradient(135deg,var(--tone-mulch-a),var(--tone-mulch-b))}
.hill{background:linear-gradient(135deg,var(--tone-land-a),var(--tone-land-b))}
.digger{background:linear-gradient(135deg,var(--tone-steel-a),var(--tone-steel-b))}
.sky-dig{background:linear-gradient(135deg,var(--tone-sky-a),var(--tone-sky-b))}
.dot{display:inline-block;border-radius:50%}
.topbar{background:var(--ink);color:#fff;display:flex;align-items:center;justify-content:space-between}
.topbar .social{display:flex;gap:8px}
.topbar .social .dot{background:#fff}
.topbar .phone{background:var(--red);height:100%;display:flex;align-items:center;font-family:"Montserrat",sans-serif;font-weight:700}
.brand{font-family:"Montserrat",sans-serif;font-weight:800;color:var(--red);display:flex;align-items:center;gap:6px;line-height:1}
.brand .sq{background:var(--red);display:inline-block}
.rule{display:inline-block;height:1px;background:var(--red);vertical-align:middle}
h2{font-family:"Montserrat",sans-serif;font-weight:800;line-height:1.02}

.desktop{left:50px;width:820px;height:1870px}
.desktop .topbar{height:30px;padding-left:80px;font-size:8px}
.desktop .topbar .dot{width:10px;height:10px}
.desktop .topbar .phone{padding:0 20px;font-size:11px}
.desktop .nav{height:55px;display:flex;align-items:center;padding:0 85px;justify-content:space-between}
.desktop .brand{font-size:14px}
.desktop .brand .sq{width:10px;height:10px}
.desktop .menu{display:flex;gap:44px;font-size:9px;color:#444;align-items:center}
.desktop .menu .on{font-weight:600;color:var(--ink)}
.desktop .menu .cta{color:var(--red);font-weight:600}
.desktop .hero{margin:0 8px;height:250px;position:relative}
.desktop .hero-panel{position:absolute;left:0;top:57px;width:355px;height:133px;background:rgba(20,20,20,.85);display:flex;align-items:center;padding-left:78px}
.desktop .hero-panel h1{font:800 38px "Montserrat",sans-serif;color:#fff}
.split{display:flex;height:390px}
.split>div{width:50%}
.copy{padding:0 85px}
.desktop .topsoil .copy{padding-top:80px}
.desktop .copy h2{font-size:34px;margin-bottom:22px}
.desktop .copy h2 .rule{width:30px;margin-left:12px}
.desktop .copy p{font-size:11px;line-height:1.5;font-weight:300;color:#444;margin-bottom:14px;max-width:255px}
.excavation .copy{background:var(--ink);padding-top:95px;padding-left:62px}
.excavation .copy h2{color:#fff}
.excavation .copy p{color:#ccc !important;max-width:265px}
.desktop .contact{height:515px;position:relative;background:linear-gradient(180deg,#fff 80%,#f4f4f4)}
.desktop .contact .photo{position:absolute;left:66px;top:76px;width:684px;height:357px}
.contact-card{position:absolute;background:var(--red);color:#fff}
.desktop .contact-card{left:361px;top:144px;width:320px;height:222px;padding:48px 24px 0 24px}
.contact-card h3{font:800 22px "Montserrat",sans-serif}
.contact-card h3 .rule{background:#fff;width:30px;margin-left:10px;opacity:.7}
.contact-card p{font-size:10px;font-weight:300;line-height:1.45;margin:14px 0 18px;max-width:250px}
.btn{display:inline-block;background:#fff;color:var(--red);font:700 8px "Montserrat",sans-serif;padding:9px 20px}
.desktop .footer{height:186px;background:var(--ink-2);color:#fff;display:flex;padding:40px 0 0 85px}
.footer h4{font:700 12px "Montserrat",sans-serif;margin-bottom:18px}
.footer .item{font-size:8px;color:var(--light);font-weight:300;line-height:1.5;display:flex;gap:10px;margin-bottom:12px}
.footer svg{flex:none}
.footer .links{font-size:8px;color:var(--light);font-weight:300;line-height:2.5}
.socials{display:flex;gap:8px;margin-top:14px}
.socials .dot{width:20px;height:20px}
.desktop .col-info{width:220px;padding-right:20px;border-right:1px solid #333}
.desktop .col-links{width:200px;padding-left:60px}
.desktop .col-others{width:200px}
.desktop .copyright{height:47px;background:var(--ink-3);color:#888;font-size:7px;display:flex;align-items:center;padding-left:85px;position:relative}
.totop{position:absolute;background:var(--red);display:flex;align-items:center;justify-content:center}
.desktop .totop{right:85px;top:0;width:44px;height:47px}

.mobile{left:920px;width:230px;height:2100px}
.mobile .topbar{height:25px;padding-left:12px}
.mobile .topbar .dot{width:9px;height:9px}
.mobile .topbar .phone{padding:0 10px;font-size:9px}
.mobile .nav{height:37px;display:flex;align-items:center;justify-content:space-between;padding:0 12px}
.mobile .brand{font-size:11px}
.mobile .brand .sq{width:8px;height:8px}
.burger{width:30px;display:flex;flex-direction:column;gap:4px}
.burger span{height:1px;background:#555}
.mobile .hero{height:154px;position:relative}
.mobile .hero-panel{position:absolute;left:0;top:38px;width:185px;height:80px;background:rgba(20,20,20,.85);display:flex;align-items:center;padding-left:20px}
.mobile .hero-panel h1{font:800 24px "Montserrat",sans-serif;color:#fff}
.mobile .copy{padding:0 12px}
.mobile .m-topsoil{height:252px;padding-top:46px}
.mobile h2{font-size:21px;margin-bottom:12px}
.mobile h2 .rule{width:22px;margin-left:8px}
.mobile .copy p{font-size:8px;line-height:1.45;font-weight:300;color:#555;margin-bottom:10px}
.mobile .m-exc{height:260px;background:var(--ink);padding-top:50px}
.mobile .m-exc h2{color:#fff}
.mobile .m-exc p{color:#ccc}
.mobile .m-contact{height:250px;margin:57px 8px 92px;position:relative}
.mobile .m-contact .photo{width:100%;height:100%}
.mobile .contact-card{left:20px;top:42px;width:195px;height:192px;padding:26px 14px 0}
.mobile .contact-card h3{font-size:15px;line-height:1.1}
.mobile .contact-card p{font-size:7px;margin:10px 0 12px}
.mobile .btn{font-size:7px;padding:7px 16px}
.mobile .footer{height:533px;background:var(--ink-2);color:#fff;padding:40px 28px 0;position:relative}
.mobile .footer h4{margin-bottom:16px;font-size:12px}
.mobile .footer .block{margin-bottom:26px}
.mobile .footer .links{line-height:2.6}
.mobile .copyright{position:absolute;left:0;right:0;bottom:0;height:48px;border-top:1px solid #333;color:#888;font-size:7px;text-align:center;padding-top:14px;line-height:1.5}
.mobile .totop{right:8px;bottom:56px;width:36px;height:36px}
</style>
</head>
<body>

<div class="label label-desktop">DESKTOP</div>
<div class="label label-mobile">MOBILE</div>

<section class="screen desktop">
  <div class="topbar">
    <div class="social"><span class="dot"></span><span class="dot"></span></div>
    <span>Now until further notice we will only be doing deliveries. No retail pick up.</span>
    <span class="phone">555-210-8834</span>
  </div>
  <header class="nav">
    <div class="brand"><span class="sq"></span>HOLLOWBROOK LOAM</div>
    <nav class="menu">
      <span>Home</span><span class="on">About</span><span>Services</span><span>Product &amp; pricing</span>
      <span class="cta">Contact <span class="rule" style="width:30px;margin-left:6px"></span></span>
    </nav>
  </header>
  <div class="hero">
    <div class="photo mulch" role="img" aria-label="Gloved hands holding red dyed mulch" style="width:100%;height:100%"></div>
    <div class="hero-panel"><h1>About Us</h1></div>
  </div>
  <div class="split topsoil">
    <div class="copy">
      <h2>Topsoil<span class="rule"></span></h2>
      <p>Our emphasis is to produce the very best quality topsoil for the best results! Our topsoil and organics make quality ready-made soils and lawn amendments. We can custom blend any products which include leaf mulch and Brannock compost to make the perfect mixtures for your needs.</p>
      <p>Contractors, landscapers, nurseries, homeowners and wholesales are welcomed.</p>
    </div>
    <div class="photo hill" role="img" aria-label="Yellow wheel loader working on a soil mound on a green hill"></div>
  </div>
  <div class="split excavation">
    <div class="photo digger" role="img" aria-label="Orange excavator bucket against a bright sky"></div>
    <div class="copy">
      <h2>Excavation<br>Services<span class="rule"></span></h2>
      <p>A leading Excavating Contractor in the NOVA area. I provide my clients with a comprehensive approach to contracting and specialize in a wide range of services. Ever since starting out as a professional Excavating Contractor, I've prioritized serving my clients' needs and satisfaction above everything else. I take care of all the small details so you don't have to.</p>
    </div>
  </div>
  <div class="contact">
    <div class="photo sky-dig" role="img" aria-label="Yellow excavator digging under a blue sky"></div>
    <div class="contact-card">
      <h3>Contact us Today<span class="rule"></span></h3>
      <p>Whether you are looking for a excavation contractor or simply interested in our products, get in touch today to bring your vision to life!</p>
      <span class="btn">Get a Quote &nbsp;›</span>
    </div>
  </div>
  <footer class="footer">
    <div class="col-info">
      <h4>Contact info</h4>
      <div class="item"><svg width="9" height="11" viewBox="0 0 10 12"><path d="M5 0a4 4 0 0 1 4 4c0 3-4 8-4 8S1 7 1 4a4 4 0 0 1 4-4z" fill="#b5202b"/><circle cx="5" cy="4" r="1.5" fill="#1c1c1c"/></svg><span>4180 Fenwick Road, Marlow, Virginia 20188, United States</span></div>
      <div class="item"><svg width="10" height="10" viewBox="0 0 10 10"><path d="M2 0l2 2.5-1.2 1.3a6 6 0 0 0 3.4 3.4L7.5 6 10 8l-1.5 2C4 10 0 6 0 1.5z" fill="#b5202b"/></svg><span>555-210-8834</span></div>
      <div class="item"><svg width="10" height="8" viewBox="0 0 10 8"><rect width="10" height="8" fill="#b5202b"/><path d="M0 0l5 4 5-4" stroke="#1c1c1c" fill="none"/></svg><span>info@rkqmo.com</span></div>
    </div>
    <div class="col-links">
      <h4>Quick links</h4>
      <div class="links">Home<br>About<br>Services<br>Product &amp; pricing<br>Contact</div>
    </div>
    <div class="col-others">
      <h4>Others</h4>
      <div class="item" style="max-width:170px">Now until further notice we will only be doing deliveries. No retail pick up at this time.</div>
      <div class="socials"><span class="dot" style="background:#3b5bb5"></span><span class="dot" style="background:#d6336c"></span></div>
    </div>
  </footer>
  <div class="copyright">Copyright © 2020 Hollowbrook Loam - All Rights Reserved.
    <div class="totop"><svg width="12" height="12" viewBox="0 0 12 12"><path d="M2 6l4-4 4 4M2 11l4-4 4 4" stroke="#fff" stroke-width="1.5" fill="none"/></svg></div>
  </div>
</section>

<section class="screen mobile">
  <div class="topbar">
    <div class="social"><span class="dot"></span><span class="dot"></span></div>
    <span class="phone">555-210-8834</span>
  </div>
  <header class="nav">
    <div class="brand"><span class="sq"></span>HOLLOWBROOK</div>
    <div class="burger"><span></span><span></span><span></span></div>
  </header>
  <div class="hero">
    <div class="photo mulch" role="img" aria-label="Hands holding red mulch with green plants behind" style="width:100%;height:100%"></div>
    <div class="hero-panel"><h1>About Us</h1></div>
  </div>
  <div class="copy m-topsoil">
    <h2>Topsoil<span class="rule"></span></h2>
    <p>Our emphasis is to produce the very best quality topsoil for the best results! Our topsoil and organics make quality ready-made soils and lawn amendments. We can custom blend any products which include leaf mulch and Brannock compost to make the perfect mixtures for your needs.</p>
    <p>Contractors, landscapers, nurseries, homeowners and wholesales are welcomed.</p>
  </div>
  <div class="photo hill" role="img" aria-label="Yellow wheel loader on a soil mound" style="height:220px"></div>
  <div class="copy m-exc">
    <h2>Excavation<br>Services</h2>
    <p>A leading Excavating Contractor in the NOVA area. I provide my clients with a comprehensive approach to contracting and specialize in a wide range of services. Ever since starting out as a professional Excavating Contractor, I've prioritized serving my clients' needs and satisfaction above everything else. I take care of all the small details so you don't have to.</p>
  </div>
  <div class="photo digger" role="img" aria-label="Orange excavator bucket against a bright sky" style="height:220px"></div>
  <div class="m-contact">
    <div class="photo sky-dig" role="img" aria-label="Yellow excavator digging under a blue sky"></div>
    <div class="contact-card">
      <h3>Contact us<br>Today<span class="rule"></span></h3>
      <p>Whether you are looking for a excavation contractor or simply interested in our products, get in touch today to bring your vision to life!</p>
      <span class="btn">Get a Quote &nbsp;›</span>
    </div>
  </div>
  <footer class="footer">
    <div class="block">
      <h4>Contact info</h4>
      <div class="item"><svg width="9" height="11" viewBox="0 0 10 12"><path d="M5 0a4 4 0 0 1 4 4c0 3-4 8-4 8S1 7 1 4a4 4 0 0 1 4-4z" fill="#b5202b"/><circle cx="5" cy="4" r="1.5" fill="#1c1c1c"/></svg><span>4180 Fenwick Road, Marlow, Virginia 20188, United States</span></div>
      <div class="item"><svg width="10" height="10" viewBox="0 0 10 10"><path d="M2 0l2 2.5-1.2 1.3a6 6 0 0 0 3.4 3.4L7.5 6 10 8l-1.5 2C4 10 0 6 0 1.5z" fill="#b5202b"/></svg><span>555-210-8834</span></div>
      <div class="item"><svg width="10" height="8" viewBox="0 0 10 8"><rect width="10" height="8" fill="#b5202b"/><path d="M0 0l5 4 5-4" stroke="#1c1c1c" fill="none"/></svg><span>info@rkqmo.com</span></div>
    </div>
    <div class="block">
      <h4>Quick links</h4>
      <div class="links">Home<br>About<br>Services<br>Product &amp; pricing<br>Contact</div>
    </div>
    <div class="block">
      <h4>Others</h4>
      <div class="item">Now until further notice we will only be doing deliveries. No retail pick up at this time.</div>
      <div class="socials"><span class="dot" style="background:#3b5bb5"></span><span class="dot" style="background:#d6336c"></span></div>
    </div>
    <div class="totop"><svg width="12" height="12" viewBox="0 0 12 12"><path d="M2 6l4-4 4 4M2 11l4-4 4 4" stroke="#fff" stroke-width="1.5" fill="none"/></svg></div>
    <div class="copyright">Copyright © 2020 Hollowbrook Loam -<br>All Rights Reserved.</div>
  </footer>
</section>

</body>
</html>
```